VANDIR/ VANDIR GREY Business Card

We have two brands that we would like to show one 1 business card (front and back). We would to incorporate two different logos on one card (VANDIR and VANDIR GREY). Card can be two sided. Simple, sleek and professional.

We are a senior living provider.

www.vandir-example.com
www.vandirgrey-example.com

Target Market(s)

Professionals

Industry/Entity Type

Business

Font styles to use
Serif

Colors

Designer to choose colors to be used in the design.

Requirements
Must have
• Space for EMAIL, PHONE, WEBSITE
Nice to have
• Raised lettering or gloss lettering

```html
<!DOCTYPE html>
<html lang="en">
<head>
<meta charset="utf-8">
<title>Vandir / Vandir Grey Business Cards</title>
<link rel="stylesheet" href="https://fonts.googleapis.com/css2?family=Marcellus&family=Open+Sans:wght@300;400&display=swap">
<style>
  :root {
    --backdrop: #505050;
    --card: #000000;
    --gold: #c09a48;
    --white: #ffffff;
    --divider: #d9d9d9;
  }
  * { box-sizing: border-box; margin: 0; padding: 0; }
  html, body {
    width: 1200px;
    height: 1200px;
    overflow: hidden;
    background: var(--backdrop);
  }
  .canvas {
    position: relative;
    width: 1200px;
    height: 1200px;
  }
  .card {
    position: absolute;
    top: 465px;
    width: 486px;
    height: 270px;
    background: var(--card);
    color: var(--white);
    overflow: hidden;
  }
  .card--vandir { left: 72px; }
  .card--vandir-grey { left: 643px; top: 468px; }

  .brand {
    position: absolute;
    left: 0;
    right: 0;
    display: flex;
    justify-content: center;
    align-items: center;
    gap: 14px;
  }
  .card--vandir .brand { top: 92px; }
  .card--vandir-grey .brand { top: 82px; }

  .brand__square {
    width: 30px;
    height: 30px;
    background: var(--gold);
    flex: none;
  }
  .brand__lockup {
    display: flex;
    flex-direction: column;
  }
  .brand__name {
    font-family: "Marcellus", serif;
    font-size: 40px;
    line-height: 1;
    letter-spacing: 0.02em;
  }
  .brand__name--gold { color: var(--gold); }
  .brand__name--white { color: var(--white); font-size: 36px; }
  .brand__tagline {
    margin-top: 4px;
    font-family: "Open Sans", sans-serif;
    font-weight: 300;
    font-size: 15px;
    color: var(--white);
    letter-spacing: 0.01em;
  }

  .contact {
    position: absolute;
    left: 0;
    right: 0;
    top: 216px;
    display: flex;
    justify-content: center;
    align-items: center;
    font-family: "Open Sans", sans-serif;
    font-weight: 400;
    font-size: 11.5px;
    line-height: 22px;
    color: var(--white);
    white-space: nowrap;
  }
  .contact__item { padding: 0 7px; }
  .contact__item + .contact__item { border-left: 1px solid var(--divider); }
</style>
</head>
<body>
  <main class="canvas">
    <section class="card card--vandir" aria-label="Vandir business card">
      <div class="brand">
        <span class="brand__square"></span>
        <span class="brand__name brand__name--gold">VANDIR</span>
      </div>
      <p class="contact">
        <span class="contact__item">+123 456 7890</span>
        <span class="contact__item">vandir@mail-example.com</span>
        <span class="contact__item">www.vandir-example.com</span>
      </p>
    </section>

    <section class="card card--vandir-grey" aria-label="Vandir Grey business card">
      <div class="brand">
        <span class="brand__square"></span>
        <div class="brand__lockup">
          <span class="brand__name brand__name--white">VANDIR GREY</span>
          <span class="brand__tagline">Executive Personal Care Services</span>
        </div>
      </div>
      <p class="contact">
        <span class="contact__item">+123 456 7890</span>
        <span class="contact__item">vandirgrey@mail-example.com</span>
        <span class="contact__item">www.vandirgrey-example.com</span>
      </p>
    </section>
  </main>
</body>
</html>
```